bavarian Beer festivals and Velmarunde

create a double sided Rack card for a Bavarian beer and velmarunde tours. We can use the template you have already created for the other brochures.
how does that sound?

We will be focusing on higher end clientele. So it will need to reflect that n the verbiage used. As well as the font and grafiks

I wil be preparing a document with all of the details on it. So that I can convey what I would like stated on the flyer.

• Please use the previous front and back page background pictures.

```html
<!DOCTYPE html>
<html lang="en">
<head>
<meta charset="utf-8">
<title>Bavarian Beer and Velmarunde – Rack Card</title>
<link href="https://fonts.googleapis.com/css2?family=Kaushan+Script&family=Germania+One&family=Federo&family=Raleway:wght@300;400;500&family=Montserrat:wght@400;500&display=swap" rel="stylesheet">
<style>
  :root{
    --page:#ececec;
    --card:#0d0a08;
    --amber:#f39a1e;
    --orange:#f0661a;
    --gold:#f2b230;
    --yellow:#ffd21c;
    --white:#ffffff;
    --text:#e8e2da;
    --band:#1a110b;
  }
  *{margin:0;padding:0;box-sizing:border-box}
  html,body{width:1118px;height:1200px;overflow:hidden;background:var(--page)}
  .sheet{position:relative;width:1118px;height:1200px}
  .card{position:absolute;top:20px;width:530px;height:1160px;overflow:hidden;background:var(--card);color:var(--white);box-shadow:0 6px 18px rgba(0,0,0,.25)}
  .card--front{left:20px}
  .card--back{left:568px}
  .backdrop{position:absolute;inset:0}
  .card--front .backdrop{background:radial-gradient(ellipse at 60% 45%,#3a2213 0%,#1d120a 55%,#0b0806 100%)}
  .card--front .barrels{position:absolute;left:0;right:0;bottom:250px;height:190px;background:linear-gradient(180deg,rgba(70,38,18,0) 0%,#3b2110 45%,#1a0f08 100%)}
  .card--back .backdrop{background:radial-gradient(ellipse at 40% 35%,#2a1a0f 0%,#140d08 50%,#080605 100%)}
  .card--back .barrels{position:absolute;left:0;right:0;top:760px;height:260px;background:linear-gradient(180deg,rgba(60,32,16,0) 0%,#2c180c 50%,rgba(10,7,5,0) 100%)}
  .centered{position:absolute;left:0;right:0;text-align:center}
  .title-script{font-family:"Kaushan Script",cursive;color:var(--white)}
  .title-beer{font-family:"Germania One",serif;line-height:1;background:linear-gradient(180deg,var(--amber) 0%,var(--orange) 70%,#c6440f 100%);-webkit-background-clip:text;background-clip:text;color:transparent}
  .title-and{font-family:"Germania One",serif;color:var(--white);display:flex;justify-content:center;align-items:center;gap:12px}
  .title-and .rule{display:block;height:1px;background:var(--text);opacity:.8}
  .ribbon{position:absolute;left:50%;transform:translateX(-50%);display:flex;align-items:center;justify-content:center;background:linear-gradient(180deg,#2a1a0f,var(--band));border:2px solid var(--white)}
  .ribbon-text{font-family:"Raleway",sans-serif;font-weight:500;color:var(--amber);letter-spacing:3px;white-space:nowrap}
  .photo-drinks{position:absolute;left:0;top:200px;width:280px;height:610px;background:radial-gradient(ellipse at 60% 75%,#f7a53a 0%,#c8681c 22%,#5b3513 50%,rgba(20,12,6,0) 75%)}
  .event{position:absolute;right:16px;width:250px;text-align:center;white-space:nowrap}
  .event-date{top:440px;font-family:"Federo",sans-serif;font-size:78px;line-height:1}
  .event-month{top:522px;font-family:"Federo",sans-serif;font-size:36px;line-height:1;color:var(--yellow);letter-spacing:13px;padding-left:13px}
  .event-goes{top:566px;font-family:"Federo",sans-serif;font-size:38px;line-height:1}
  .divider{position:absolute;height:1px;background:var(--text);opacity:.55}
  .event-venue{top:646px;font-family:"Raleway",sans-serif;font-weight:300;font-size:58px;line-height:1;color:var(--gold)}
  .event-address{top:708px;font-family:"Raleway",sans-serif;font-weight:400;font-size:16px;color:var(--text)}
  .perks{position:absolute;left:24px;right:24px;top:878px;display:flex;justify-content:space-between;align-items:center}
  .perk{flex:1;text-align:center;font-family:"Raleway",sans-serif;font-size:23px;line-height:1.2}
  .perk--gold{color:var(--gold)}
  .perk-sep{width:1px;height:52px;background:var(--text);opacity:.7}
  .join{top:1000px;font-family:"Raleway",sans-serif;font-size:24px}
  .join em{font-style:normal;color:var(--gold)}
  .note{top:1048px;padding:0 72px;font-family:"Raleway",sans-serif;font-size:15.5px;line-height:1.42;color:var(--text)}
  .section-head{font-family:"Kaushan Script",cursive;font-size:30px;font-weight:400;color:var(--white)}
  .section-head span{color:var(--gold)}
  .section-body{padding:0 50px;font-family:"Montserrat",sans-serif;font-size:15px;line-height:1.45;color:var(--text)}
  .web-icon{position:absolute;left:50%;transform:translateX(-50%);top:1036px}
  .web-address{top:1092px;font-family:"Montserrat",sans-serif;font-size:19px;letter-spacing:5px;color:var(--gold)}
</style>
</head>
<body>
<main class="sheet">

  <section class="card card--front">
    <div class="backdrop" role="img" aria-label="Dark cellar background with wooden beer barrels"></div>
    <div class="barrels" role="img" aria-label="Wooden barrel the drinks stand on"></div>
    <div class="photo-drinks" role="img" aria-label="Photo of a chilled beer bottle and a frothy glass of amber beer"></div>

    <div class="centered title-script" style="top:26px;font-size:64px;line-height:1;padding-left:30px">Bavarian</div>
    <div class="centered title-beer" style="top:92px;font-size:170px;padding-left:20px">BEER</div>
    <div class="centered title-and" style="top:250px;font-size:26px;padding-left:30px">
      <span class="rule" style="width:80px"></span>AND<span class="rule" style="width:80px"></span>
    </div>
    <div class="ribbon" style="top:298px;margin-left:20px;width:270px;height:48px" role="img" aria-label="Scroll ribbon banner">
      <span class="ribbon-text" style="font-size:24px">VELMARUNDE</span>
    </div>
    <div class="divider" style="top:372px;left:220px;width:120px"></div>

    <div class="event event-date">DATE</div>
    <div class="event event-month">MONTH</div>
    <div class="event event-goes">GOES HERE</div>
    <div class="divider" style="top:628px;right:91px;width:100px"></div>
    <div class="event event-venue">VENUE</div>
    <div class="event event-address">ADDRESS GOES HERE</div>

    <div class="perks">
      <div class="perk perk--gold">LIVE<br>MUSIC</div>
      <span class="perk-sep"></span>
      <div class="perk">FREE<br>PARKING</div>
      <span class="perk-sep"></span>
      <div class="perk perk--gold">FREE<br>ENTER</div>
    </div>
    <div class="divider" style="top:970px;left:225px;width:80px"></div>
    <div class="centered join"><em>Come and Join</em> For more Details</div>
    <p class="centered note">Lorem Ipsum is simply dummy text of the printing and typesetting industry. Lorem Ipsum has been the industry's standard dummy text ever since the 1500s,</p>
  </section>

  <section class="card card--back">
    <div class="backdrop" role="img" aria-label="Dark background with a faint beer bottle"></div>
    <div class="barrels" role="img" aria-label="Faint wooden barrels in shadow"></div>

    <div class="centered title-script" style="top:40px;font-size:48px;line-height:1;padding-left:10px">Bavarian</div>
    <div class="centered title-beer" style="top:88px;font-size:118px">BEER</div>
    <div class="centered title-and" style="top:205px;font-size:20px">
      <span class="rule" style="width:60px"></span>AND<span class="rule" style="width:60px"></span>
    </div>
    <div class="ribbon" style="top:242px;width:210px;height:38px" role="img" aria-label="Scroll ribbon banner">
      <span class="ribbon-text" style="font-size:18px">VELMARUNDE</span>
    </div>

    <h2 class="centered section-head" style="top:352px">Headline 1 <span>Goes Here</span></h2>
    <div class="divider" style="top:402px;left:235px;width:60px"></div>
    <p class="centered section-body" style="top:418px">Lorem Ipsum is simply dummy text of the printing and typesetting industry. Lorem Ipsum has been the industry's standard dummy text ever since the 1500s, Lorem Ipsum is simply dummy text of the printing and typesetting industry. Lorem Ipsum has been the industry's standard dummy text ever since the 1500s,</p>

    <h2 class="centered section-head" style="top:580px">Headline 2 <span>Goes Here</span></h2>
    <div class="divider" style="top:630px;left:235px;width:60px"></div>
    <p class="centered section-body" style="top:646px">Lorem Ipsum is simply dummy text of the printing and typesetting industry. Lorem Ipsum has been the industry's standard dummy text ever since the 1500s, Lorem Ipsum is simply dummy text of the printing and typesetting industry. Lorem Ipsum has been the industry's standard dummy text ever since the 1500s,</p>

    <h2 class="centered section-head" style="top:808px">Headline 3 <span>Goes Here</span></h2>
    <div class="divider" style="top:858px;left:235px;width:60px"></div>
    <p class="centered section-body" style="top:874px">Lorem Ipsum is simply dummy text of the printing and typesetting industry. Lorem Ipsum has been the industry's standard dummy text ever since the 1500s, Lorem Ipsum is simply dummy text of the printing and typesetting industry. Lorem Ipsum has been the industry's standard dummy text ever since the 1500s,</p>

    <svg class="web-icon" width="40" height="40" viewBox="0 0 40 40" aria-hidden="true">
      <g fill="none" stroke="#8a5a1c" stroke-width="2">
        <circle cx="20" cy="20" r="17"/>
        <ellipse cx="20" cy="20" rx="7" ry="17"/>
        <line x1="3" y1="20" x2="37" y2="20"/>
        <path d="M6 11 H34 M6 29 H34"/>
      </g>
    </svg>
    <div class="centered web-address">www.yourwebite.com</div>
  </section>

</main>
</body>
</html>
```